Website design for dressage horse training business

Looking to develop a new website design for a dressage horse training website. We want to change from a single landing page to one with multiple pages.
You are free to use your creativity to design the main landing page. This is the only page you need to design at this point. I would encourage looking at other Dressage Training websites to get a feel for what is typically on them. A few websites are listed below although I think the design of them could be better.
Notes:
- Menu to include: Home, Services, News Room, Blog, About Us, Contact,
- FAQ section on main page
- Logo to remain the same - the logo attached is not the correct color so change to match existing color.
- Change 'Sponsors' to 'Partnerships' on main page
Here is the link to the current site:
https://larkvalebarn.com/
Example sites
https://www.quillbrookstablesna.com/
https://corinnahaldwickdressage.com/
Older women with disposable income

```html
<!DOCTYPE html>
<html lang="en">
<head>
<meta charset="utf-8">
<title>Larkvale Barn – Dressage &amp; Sport Horse Training</title>
<link href="https://fonts.googleapis.com/css2?family=Cinzel:wght@400;700&family=Roboto:wght@400;500;700&display=swap" rel="stylesheet">
<style>
:root{
  --tan:#b98d62;
  --ink:#141414;
  --text-grey:#8a8a8a;
  --white:#ffffff;
  --light:#f1efec;
  --neutral:#e6e6e6;
}
*{box-sizing:border-box;margin:0;padding:0}
html,body{width:1200px;height:4370px;overflow:hidden}
body{font-family:'Roboto',sans-serif;color:var(--ink);background:var(--white);position:relative}
.section{position:absolute;left:0;width:1200px;overflow:hidden}
.btn{position:absolute;display:flex;align-items:center;justify-content:center;background:var(--tan);color:var(--white);
  font-family:'Roboto',sans-serif;font-weight:700;font-size:15px;letter-spacing:.3px;border-radius:32px;text-transform:uppercase}
.photo{position:absolute}

/* header */
.site-header{top:0;height:81px;background:var(--white)}
.brand{position:absolute;left:0;width:1200px;top:18px;text-align:center;font-family:'Cinzel',serif;font-size:30px;color:var(--tan);letter-spacing:2px}
.phone{position:absolute;display:flex;align-items:center;gap:12px;font-weight:700;font-size:23px;color:var(--ink)}
.site-header .phone{left:820px;top:20px}

/* nav */
.main-nav{top:81px;height:51px;background:var(--tan)}
.main-nav ul{list-style:none;display:flex;position:absolute;left:187px;top:0;height:51px}
.main-nav li{height:51px;display:flex;align-items:center;padding:0 22px;color:var(--white);font-size:15px;text-transform:uppercase}
.main-nav li.active{background:#383838}

/* hero */
.hero{top:132px;height:591px;background:#000}
.hero .photo{left:0;top:0;width:520px;height:591px;background:radial-gradient(ellipse at 45% 40%,#5a5a5a 0%,#2c2c2c 40%,#000 75%)}
.hero h1{position:absolute;left:579px;top:158px;font-family:'Cinzel',serif;font-weight:400;font-size:64px;color:var(--white);line-height:1;white-space:nowrap}
.hero p{position:absolute;left:579px;top:266px;font-size:27px;line-height:39px;color:var(--white);font-weight:500}
.hero .btn{left:580px;top:379px;width:184px;height:64px}
.dots{position:absolute;top:522px;left:558px;display:flex;gap:10px}
.dots span{width:10px;height:10px;border-radius:50%;background:var(--white)}
.dots span.on{background:#b0282b}

/* about */
.about{top:723px;height:640px;background:var(--light)}
.about .photo{inset:0;background:linear-gradient(100deg,#ecebe8 0%,#e0dcd6 40%,#f4f2ef 60%,#e6e2dc 100%)}
.title-dark{position:absolute;font-family:'Cinzel',serif;font-weight:700;font-size:60px;line-height:66px;white-space:nowrap}
.title-dark .accent{color:var(--tan);display:block;font-weight:400}
.about .title-dark{left:146px;top:78px;color:var(--ink);font-size:50px;line-height:64px}
.about .copy{position:absolute;left:574px;top:84px;width:484px;font-size:14px;line-height:24px;color:var(--text-grey)}
.about .copy p+p{margin-top:24px}
.about .btn{left:574px;top:502px;width:162px;height:56px}

/* featured horse */
.featured{top:1363px;height:697px;background:var(--ink)}
.featured .photo{left:600px;top:0;width:600px;height:697px;background:linear-gradient(160deg,#d9d9d9 0%,#a9a9a9 35%,#555 65%,#2b2b2b 100%)}
.featured .title-dark{left:146px;top:70px;color:var(--white)}
.featured .copy{position:absolute;left:146px;top:232px;width:424px;font-size:14.5px;line-height:24px;color:var(--white)}
.featured .btn{left:146px;top:559px;width:162px;height:56px}

/* bands */
.band{height:80px;background:var(--tan);display:flex;align-items:center;justify-content:center;color:var(--white);font-family:'Cinzel',serif;font-size:56px}
.band-partners{top:2060px}
.band-faq{top:3441px}

/* partners */
.partners{top:2140px;height:604px;background:var(--white)}
.partner{position:absolute;top:0;width:460px;text-align:center}
.partner-a{left:127px}
.partner-b{left:615px}
.badge{position:absolute;top:72px;left:145px;width:170px;height:92px;background:var(--neutral)}
.partner h3{position:absolute;top:208px;width:460px;font-size:27px;font-weight:500;color:#222}
.partner p{position:absolute;top:265px;left:0;width:460px;font-size:14px;line-height:24px;color:var(--text-grey)}
.partner .btn{top:468px;left:149px;width:162px;height:56px}

/* services */
.services{top:2744px;height:697px;background:#222}
.service{position:absolute;top:0;width:600px;height:697px}
.service-training{left:0;background:linear-gradient(180deg,#4a4a4a 0%,#2f2f2f 45%,#151515 100%)}
.service-lessons{left:600px;background:linear-gradient(180deg,#3e3e3e 0%,#2a2a2a 45%,#121212 100%)}
.service h2{position:absolute;top:318px;left:146px;font-family:'Cinzel',serif;font-weight:700;font-size:58px;color:var(--white);line-height:1}
.service p{position:absolute;top:420px;left:146px;width:430px;font-size:14px;line-height:24px;color:var(--white)}
.service .btn{top:522px;left:146px;width:162px;height:56px}
.service-lessons h2,.service-lessons p,.service-lessons .btn{left:106px}

/* faq */
.faq{top:3521px;height:545px;background:var(--light)}
.faq .photo{inset:0;background:linear-gradient(90deg,#e4e1dc 0%,#f6f5f3 45%,#f6f5f3 60%,#e2ded8 100%)}
.faq-list{position:absolute;left:295px;top:64px;width:606px}
.faq-item{position:relative;height:48px;background:var(--white);border-radius:24px;box-shadow:0 2px 8px rgba(0,0,0,.12);display:flex;align-items:center;padding-left:34px;font-size:14.5px;color:#222;margin-bottom:14px}
.faq-item .toggle{position:absolute;right:6px;top:6px;width:36px;height:36px;border-radius:50%;background:var(--tan);display:flex;align-items:center;justify-content:center}
.faq-item.open .toggle{background:#111}
.faq-answer{padding:6px 34px 22px 28px;font-size:13px;line-height:24px;color:var(--text-grey);margin-top:-6px}

/* footer */
.site-footer{top:4066px;height:304px;background:#1b1b1b}
.footer-brand{position:absolute;left:146px;top:56px;font-family:'Cinzel',serif;font-size:34px;color:var(--tan);letter-spacing:1px;white-space:nowrap}
.social{position:absolute;left:508px;top:65px;display:flex;gap:28px}
.social span{width:34px;height:34px;border-radius:50%;border:3px solid var(--white)}
.site-footer .phone{left:820px;top:63px;color:var(--white)}
.footer-rule{position:absolute;left:146px;top:155px;width:910px;height:1px;background:#333}
.footer-nav{position:absolute;left:0;width:1200px;top:180px;display:flex;justify-content:center;list-style:none;gap:44px;color:var(--white);font-size:15px;text-transform:uppercase;padding-right:8px}
.legal{position:absolute;left:0;width:1200px;top:256px;text-align:center;color:var(--white);font-size:12.5px}
</style>
</head>
<body>

<header class="section site-header">
  <div class="brand">Larkvale Barn</div>
  <div class="phone">
    <svg width="40" height="40" viewBox="0 0 40 40" aria-hidden="true"><circle cx="20" cy="20" r="18" fill="none" stroke="var(--tan)" stroke-width="2.5"/><path d="M13 12c1-1 2-1 3 0l2.5 3c.6.8.5 1.7-.2 2.3l-1.5 1.2c1 2.2 2.6 3.8 4.7 4.8l1.2-1.5c.6-.7 1.6-.8 2.3-.2l3 2.5c1 .9 1 2 0 3l-1.5 1.5c-1.5 1.5-9 0-13-4s-5.5-11.5-4-13z" fill="var(--tan)"/></svg>
    <span>T: 555-014-2290</span>
  </div>
</header>

<nav class="section main-nav">
  <ul>
    <li class="active">Home</li><li>Services</li><li>News Room</li><li>Blog</li><li>About Us</li><li>Partnerships</li><li>Contact</li>
  </ul>
</nav>

<section class="section hero">
  <div class="photo" role="img" aria-label="Black and white portrait of a bay dressage horse in a double bridle"></div>
  <h1>Larkvale Barn</h1>
  <p>Central Iowa’s Premier dressage<br>and sport horse training</p>
  <a class="btn">Get Started</a>
  <div class="dots"><span></span><span></span><span class="on"></span><span></span><span></span></div>
</section>

<section class="section about">
  <div class="photo" role="img" aria-label="Faded photo of the trainer with grey horses"></div>
  <h2 class="title-dark">About<span class="accent">Larkvale Barn</span></h2>
  <div class="copy">
    <p>FEI rider and trainer, Helena Varga began her riding career at a young age. She went up through the ranks of Pony Club and with an emphasis and focus in eventing. During college, Helena worked for a small breeder starting young horses. Helena loves starting young horses including starting and guiding them in a correct and quiet way to help them flourish. Her training focuses on gymnastic training incorporating ground work lunging/long lining, jumping, cavelletti and regular hacking and trail riding.</p>
    <p>Helena is a NDF Silver Medalist having competed through the FEI levels of I1. A learner at heart, Helena regularly clinics and rides with other trainers and accomplished dressage riders from across the nation to continue to pursue her goal of competing at the Grand Prix. Helena has attended the NDF L Program as well as the Instructor/Trainer program to continue her growth as a trainer and rider. Helena trains and competes yearly in the winter season in Wellington, Florida to further her knowledge and development to share with her students!</p>
  </div>
  <a class="btn">Read More</a>
</section>

<section class="section featured">
  <h2 class="title-dark">Marlowe<span class="accent">Crest</span></h2>
  <div class="copy">Marlowe Crest, “Milo,” (Cordane x Quill Regent) is a 2012, 16hh imported Hanoverian. Milo is an incredibly quiet and kind horse. He is ridden by both an amatuer and child rider. He loves to hack and is very quiet alone and with a group of horses. He has shown through first level with scores into the 70’s at both training and first level. Milo is currently solidly schooling all of second level, as well as half passes and flying changes from third level. Milo has 3 very easy to ride gaits and it is easy for riders to sit his trot. Very quiet and well mannered on the ground with vet, farrier and clipping. He has lovely confirmation with a striking head.<br>He is regularly admired at shows! Milo is very versatile<br>and game and also loves to jump!</div>
  <a class="btn">Read More</a>
  <div class="photo" role="img" aria-label="Black and white photo of a dark horse standing before flowering shrubs"></div>
</section>

<div class="section band band-partners">Partnerships</div>

<section class="section partners">
  <div class="partner partner-a">
    <div class="badge" aria-hidden="true"></div>
    <h3>Fieldcrest Saddlery</h3>
    <p>Fieldcrest Saddlery is constantly designing and researching saddles and riders to find the right blend of design and craftsmanship to fit today’s demands. Every saddle’s detail is carefully checked to be sure the workmanship and quality is there. All saddles are anatomically designed for horse and rider, hand-crafted from the finest leathers, and manufactured using the most technically advanced methods and features available.</p>
    <a class="btn">Read More</a>
  </div>
  <div class="partner partner-b">
    <div class="badge" aria-hidden="true"></div>
    <h3>Ashdown's Saddlery</h3>
    <p>My goal is to provide the best possible fit for both horse and rider whether it is a saddle you already own, one you have on trial, or one that I carry. Being a Qualified Saddle Fitter by the Guild of Saddle Fitters allows me to work with all saddle types and brands. In addition, I carry a broad range of saddles to fit your needs, both new and used. Having a multitude of saddles in my stock makes saddle shopping much easier for you.</p>
    <a class="btn">Read More</a>
  </div>
</section>

<section class="section services">
  <div class="service service-training" role="img" aria-label="Dark photo of a rider on horseback beside a wooden barn">
    <h2>Training</h2>
    <p>Larkvale Barn offers both full and half time training options with Helena Varga. There is much flexibility with both rides and/or lessons weekly in the training packages...</p>
    <a class="btn">Read More</a>
  </div>
  <div class="service service-lessons" role="img" aria-label="Dark photo of a young rider in helmet and show jacket">
    <h2>Lessons</h2>
    <p>Lessons are available for all ages of riders. Helena thoroughly enjoys working with accomplished riders looking to succeed in the show ring, as well as riders...</p>
    <a class="btn">Read More</a>
  </div>
</section>

<div class="section band band-faq">FAQ’s</div>

<section class="section faq">
  <div class="photo" role="img" aria-label="Faded photo of horses in a paddock"></div>
  <div class="faq-list">
    <div class="faq-item open">Lorem ipsum dolor sit ametconsectetur adipiscing elit?
      <span class="toggle"><svg width="14" height="14" viewBox="0 0 14 14"><rect x="2" y="6" width="10" height="2" fill="#fff"/></svg></span></div>
    <div class="faq-answer">Lorem ipsum dolor sit amet, consectetur adipiscing elit, sed do eiusmod tempor incididunt ut labore et dolore magna aliqua. Ut enim ad minim veniam, quis nostrud exercitation ullamco laboris nisi ut aliquip ex lor in reprehenderit in voluptate velit esse</div>
    <div class="faq-item">Sed ut perspiciatis unde omnis iste natus error sit?
      <span class="toggle"><svg width="14" height="14" viewBox="0 0 14 14"><rect x="2" y="6" width="10" height="2" fill="#fff"/><rect x="6" y="2" width="2" height="10" fill="#fff"/></svg></span></div>
    <div class="faq-item">Iunde omnis iste natus error sit voluptatem accusantium ?
      <span class="toggle"><svg width="14" height="14" viewBox="0 0 14 14"><rect x="2" y="6" width="10" height="2" fill="#fff"/><rect x="6" y="2" width="2" height="10" fill="#fff"/></svg></span></div>
    <div class="faq-item">Lorem ipsum dolor sit ametconsectetur adipiscing elit?
      <span class="toggle"><svg width="14" height="14" viewBox="0 0 14 14"><rect x="2" y="6" width="10" height="2" fill="#fff"/><rect x="6" y="2" width="2" height="10" fill="#fff"/></svg></span></div>
    <div class="faq-item">Iunde omnis iste natus error sit voluptatem accusantium ?
      <span class="toggle"><svg width="14" height="14" viewBox="0 0 14 14"><rect x="2" y="6" width="10" height="2" fill="#fff"/><rect x="6" y="2" width="2" height="10" fill="#fff"/></svg></span></div>
  </div>
</section>

<footer class="section site-footer">
  <div class="footer-brand">Larkvale Barn</div>
  <div class="social" aria-label="Social links"><span></span><span></span><span></span><span></span></div>
  <div class="phone">
    <svg width="40" height="40" viewBox="0 0 40 40" aria-hidden="true"><circle cx="20" cy="20" r="18" fill="none" stroke="var(--tan)" stroke-width="2.5"/><path d="M13 12c1-1 2-1 3 0l2.5 3c.6.8.5 1.7-.2 2.3l-1.5 1.2c1 2.2 2.6 3.8 4.7 4.8l1.2-1.5c.6-.7 1.6-.8 2.3-.2l3 2.5c1 .9 1 2 0 3l-1.5 1.5c-1.5 1.5-9 0-13-4s-5.5-11.5-4-13z" fill="var(--tan)"/></svg>
    <span>T: 555-014-2290</span>
  </div>
  <div class="footer-rule"></div>
  <ul class="footer-nav"><li>Home</li><li>Services</li><li>News Room</li><li>Blog</li><li>About Us</li><li>Partnerships</li><li>Contact</li></ul>
  <div class="legal">© 2020 Larkvale Barn All Rights Reserved | &nbsp;Privacy Policy &nbsp;| &nbsp;Terms and use</div>
</footer>

</body>
</html>
```